Stationery Design Project for Lakemont Kenbu Kai Karate Studio

We Need a Stationery Design for a Karate School Teaching Okinawa Shorin Ryu Karate in Lakemont, Palmora, U.S.A.

Target Market(s)

Adults Base Western Speaking aged between 25 and 65 yrs, old that handle household budgets

Industry/Entity Type

School

Requirements
Must have
• Name of business: Lakemont Kenbu Kai Karate Studio
Address: Maplecrest Plaza 38214 US Hwy. 61
Lakemont, Palmora. 33812
Phone # : 407-555-0183
email : Lakemontkenbukaistudio@samplemail.net
Logo - attatched

```html
<!DOCTYPE html>
<html lang="en">
<head>
<meta charset="utf-8">
<title>Lakemont Kenbu Kai Karate Studio – Envelope</title>
<link href="https://fonts.googleapis.com/css2?family=Mulish:wght@400;700;800&display=swap" rel="stylesheet">
<style>
  :root {
    --flap-red: #ff0000;
    --accent-olive: #cbc65a;
    --paper: #fafafa;
    --edge: #c8c8c8;
    --ink-black: #111111;
    --ink-grey: #6a6a6a;
    --title-red: #e8100f;
  }
  * { margin: 0; padding: 0; box-sizing: border-box; }
  html, body {
    width: 1200px;
    height: 815px;
    overflow: hidden;
    background: #ffffff;
    font-family: "Mulish", Arial, sans-serif;
  }
  .envelope {
    position: relative;
    width: 1195px;
    height: 811px;
    background: var(--paper);
    border: 1px solid var(--edge);
  }
  .envelope-flap {
    position: absolute;
    left: 0;
    top: 0;
    width: 1195px;
    height: 216px;
  }
  .flap-mark {
    position: absolute;
    left: 536px;
    top: 80px;
    width: 120px;
    text-align: center;
    transform: rotate(180deg);
    color: var(--ink-black);
    font-weight: 800;
    font-size: 13px;
    line-height: 1.15;
    text-transform: uppercase;
  }
  .return-address {
    position: absolute;
    left: 118px;
    top: 292px;
    display: flex;
    align-items: flex-start;
  }
  .studio-mark {
    width: 106px;
    height: 118px;
    display: flex;
    flex-direction: column;
    justify-content: center;
    align-items: center;
    text-align: center;
    color: var(--ink-black);
    font-weight: 800;
    font-size: 15px;
    line-height: 1.15;
    text-transform: uppercase;
  }
  .accent-half {
    margin: 17px 0 0 8px;
    width: 28px;
    height: 46px;
  }
  .address-block {
    margin-left: 9px;
    margin-top: 11px;
  }
  .studio-name {
    color: var(--title-red);
    font-weight: 700;
    font-size: 15.5px;
    letter-spacing: 0.6px;
    text-transform: uppercase;
    line-height: 20px;
    margin-bottom: 2px;
  }
  .address-line {
    color: var(--ink-grey);
    font-size: 16px;
    line-height: 20px;
  }
</style>
</head>
<body>
  <main class="envelope">
    <svg class="envelope-flap" viewBox="0 0 1195 216" aria-hidden="true">
      <path d="M0 214 L28 52 Q36 0 88 0 L1108 0 Q1158 0 1166 52 L1194 214 Z" fill="var(--flap-red)"/>
      <path d="M559 0 A37 37 0 0 0 633 0 Z" fill="var(--accent-olive)"/>
    </svg>
    <div class="flap-mark">Lakemont<br>Kenbu Kai<br>Karate</div>

    <section class="return-address">
      <div class="studio-mark">Lakemont<br>Kenbu Kai<br>Karate</div>
      <svg class="accent-half" viewBox="0 0 28 46" aria-hidden="true">
        <path d="M0 0 A23 23 0 0 1 0 46 Z" fill="var(--accent-olive)"/>
      </svg>
      <div class="address-block">
        <p class="studio-name">Lakemont Kenbu Kai Karate Studio</p>
        <p class="address-line">Maplecrest Plaza 38214 US Hwy. 61</p>
        <p class="address-line">Lakemont, Palmora. 33812</p>
      </div>
    </section>
  </main>
</body>
</html>
```